Valentines Day Helicopter Tour Mailer

The purpose behind this project is to design a mailer for helicopter tours around valentines day. Not sure exaclty all what to include as i'm not sure if i want to price on it yet but i want helicopters, hearts, and something interesting to draw attention to the service we will be offering. If we did include price it would be $169/ person. Size should be good for 8.5 by 11 paper

Target Market(s)

general public

```html
<!DOCTYPE html>
<html lang="en">
<head>
<meta charset="utf-8">
<title>Valentines Day Helicopter Tour Mailer</title>
<link href="https://fonts.googleapis.com/css2?family=Poppins:ital,wght@0,400;0,600;0,700;0,800;1,600&family=Lobster&display=swap" rel="stylesheet">
<style>
  :root {
    --stage: #5e5e5e;
    --ink: #050505;
    --red: #e11d24;
    --deep-red: #8e0d12;
    --white: #ffffff;
    --text-dark: #1a1a1a;
    --silver-light: #f2f2f2;
    --silver-dark: #6d6d6d;
  }
  * { margin: 0; padding: 0; box-sizing: border-box; }
  html, body { width: 1200px; height: 2192px; overflow: hidden; background: var(--stage); }
  .stage { position: relative; width: 1200px; height: 2192px; }
  .mailer {
    position: absolute; left: 60px; top: 397px;
    width: 896px; height: 1160px;
    transform: scale(1.2054); transform-origin: 0 0;
    background: var(--ink); overflow: hidden;
    font-family: "Poppins", sans-serif; color: var(--white);
    box-shadow: 0 20px 50px rgba(0,0,0,.45);
  }
  .mailer-art { position: absolute; inset: 0; width: 896px; height: 1160px; }
  .brand {
    position: absolute; left: 74px; top: 100px;
    font-weight: 700; font-size: 34px; line-height: 1; color: var(--white);
    display: flex; align-items: center; gap: 12px;
  }
  .brand-mark { width: 18px; height: 18px; border-radius: 50%; background: var(--white); }
  .headline { position: absolute; left: 74px; top: 206px; font-weight: 400; }
  .headline-big { display: block; font-weight: 700; font-size: 82px; line-height: 75px; letter-spacing: 1px; }
  .headline-sub { display: block; font-weight: 400; font-size: 38px; line-height: 46px; margin-top: 4px; }
  .headline-script { display: block; font-family: "Lobster", cursive; font-weight: 400; color: var(--red); font-size: 80px; line-height: 86px; }
  .price { position: absolute; left: 148px; top: 640px; width: 180px; text-align: center; }
  .price-amount { display: block; font-weight: 700; font-size: 62px; line-height: 64px; }
  .price-unit { display: block; color: var(--red); font-size: 24px; line-height: 26px; }
  .tour-note {
    position: absolute; left: 550px; top: 537px; padding-left: 18px;
    border-left: 3px solid var(--red);
    font-size: 28px; line-height: 37px; height: 176px; padding-top: 10px;
  }
  .tour-note strong { font-weight: 600; }
  .details { position: absolute; left: 233px; top: 928px; width: 522px; color: var(--text-dark); }
  .details-copy { font-size: 15.5px; line-height: 25px; }
  .details-copy em { color: var(--red); font-weight: 600; font-size: 21px; }
  .details-rule { border: 0; border-top: 1.5px solid var(--text-dark); margin: 14px 0 0; width: 515px; }
  .contact { display: flex; justify-content: space-between; align-items: center; width: 520px; margin-top: 12px; }
  .contact-web { font-size: 17px; }
  .contact-phone { font-weight: 600; font-size: 26px; display: flex; align-items: center; gap: 10px; }
  .contact-phone svg { width: 20px; height: 20px; }
</style>
</head>
<body>
<div class="stage">
  <div class="mailer">
    <svg class="mailer-art" viewBox="0 0 896 1160" xmlns="http://www.w3.org/2000/svg">
      <defs>
        <linearGradient id="heliPhoto" x1="0" y1="0" x2="1" y2="0.6">
          <stop offset="0" stop-color="#050505"/>
          <stop offset="0.45" stop-color="#1a2358"/>
          <stop offset="1" stop-color="#2b3a8c"/>
        </linearGradient>
        <linearGradient id="heliFade" x1="0" y1="0" x2="1" y2="0">
          <stop offset="0" stop-color="#050505"/>
          <stop offset="1" stop-color="#050505" stop-opacity="0"/>
        </linearGradient>
        <linearGradient id="cityPhoto" x1="0" y1="0" x2="0" y2="1">
          <stop offset="0" stop-color="#050505"/>
          <stop offset="0.4" stop-color="#2a1410"/>
          <stop offset="0.75" stop-color="#17151c"/>
          <stop offset="1" stop-color="#0b0e1c"/>
        </linearGradient>
        <linearGradient id="heartPhoto" x1="0" y1="0" x2="1" y2="1">
          <stop offset="0" stop-color="#e8a3b6"/>
          <stop offset="0.5" stop-color="#b8374a"/>
          <stop offset="1" stop-color="#7a1c1c"/>
        </linearGradient>
        <linearGradient id="silver" x1="0" y1="0" x2="1" y2="0">
          <stop offset="0" stop-color="var(--silver-dark)"/>
          <stop offset="0.45" stop-color="var(--silver-light)"/>
          <stop offset="1" stop-color="#3a3a3a"/>
        </linearGradient>
        <linearGradient id="redBand" x1="0" y1="0" x2="1" y2="0">
          <stop offset="0" stop-color="var(--red)"/>
          <stop offset="1" stop-color="var(--deep-red)"/>
        </linearGradient>
      </defs>
      <rect x="300" y="0" width="596" height="482" fill="url(#heliPhoto)" role="img" aria-label="Photo of a helicopter parked on a lit helipad at dusk"/>
      <rect x="300" y="0" width="220" height="482" fill="url(#heliFade)"/>
      <rect x="0" y="482" width="896" height="678" fill="url(#cityPhoto)" role="img" aria-label="Aerial night photo of a lakeside city"/>
      <path fill-rule="evenodd" fill="url(#heartPhoto)" role="img" aria-label="Heart-shaped frame showing a pink sunset over a forested river"
        d="M260 840 C150 770 50 690 55 590 C60 510 150 470 230 540 C310 460 490 480 483 580 C476 700 360 775 260 840 Z
           M250 752 C170 722 95 680 95 622 C95 565 170 555 230 610 C300 550 448 560 445 620 C440 690 330 730 250 752 Z"/>
      <path d="M150 900 C320 810 600 760 896 740 L896 800 C640 805 380 830 170 915 Z" fill="url(#redBand)"/>
      <path d="M0 1160 L0 1060 C30 1130 90 1110 100 1040 C110 960 200 880 340 840 C500 800 700 800 896 790 L896 1160 Z" fill="url(#silver)"/>
      <path d="M115 1160 C105 1055 115 980 155 935 C250 850 575 828 896 836 L896 1160 Z" fill="var(--red)"/>
      <path d="M130 1160 C120 1060 130 990 170 945 C260 862 580 842 896 850 L896 1160 Z" fill="var(--white)"/>
    </svg>

    <div class="brand"><span class="brand-mark"></span>Skylark Helicopters</div>

    <h1 class="headline">
      <span class="headline-big">TAKE</span>
      <span class="headline-big">ROMANCE</span>
      <span class="headline-sub">to New Heights on this</span>
      <span class="headline-script">Valentines Day!</span>
    </h1>

    <div class="price">
      <span class="price-amount">$169</span>
      <span class="price-unit">Per Person</span>
    </div>

    <p class="tour-note"><strong>HELICOPTER<br>TOURS</strong> Around<br>Great Lakes area<br>and beyond.</p>

    <div class="details">
      <p class="details-copy">You will feel safe at home in our helicopters because our pilots have been trained to the highest standard and we strive to be the best. <em>Come enjoy the safety, security and down right experience of a helicopter today!</em></p>
      <hr class="details-rule">
      <div class="contact">
        <span class="contact-web">www.skylarkhelicopters.com</span>
        <span class="contact-phone">
          <svg viewBox="0 0 24 24" aria-hidden="true"><path fill="#e11d24" d="M6.6 10.8a15.1 15.1 0 0 0 6.6 6.6l2.2-2.2a1 1 0 0 1 1-.25 11.4 11.4 0 0 0 3.6.6 1 1 0 0 1 1 1V20a1 1 0 0 1-1 1A17 17 0 0 1 3 4a1 1 0 0 1 1-1h3.5a1 1 0 0 1 1 1c0 1.25.2 2.45.57 3.57a1 1 0 0 1-.25 1z"/></svg>
          555-014-0271
        </span>
      </div>
    </div>
  </div>
</div>
</body>
</html>
```